Dr Mira Thalen, Orthopaedic Hand Surgeon

I am an orthopaedic hand surgeon and need business cards that reflect the surgery I do. I operate on bones, ligaments, tendons, and soft tissues. I can do microsurgery (surgery under an operating microscope) - including connecting ends of cut nerves and arteries in the fingers together. As an orthopaedic surgeon, I also fix fractures and manage orthopaedic trauma in the rest of the body. I favour black as a colour, and have some pictures of hand X-rays that you can use in the design, if you think that would look good (feel free to crop).
Updates

Hi all. Thank you for all your submissions so far. Please note that I have updated my project brief. I would like to emphasise that use of the logos that I have provided is optional, and if used, I would very much prefer the logo not to dominate the card, but add to the overall aesthetic of the card. Warm regards, Mira

Target Market(s)

Referring medical practitioners, hand therapists, patients

Industry/Entity Type

Healthcare

Contact Information for Business Card

Dr Mira Thalen
Orthopaedic Hand Surgeon
MBBS BSc (Med), MIntPH (Merit), FCWES (Ortho), FUPelV

Font styles to use
Serif

Colors

Designer to choose colors to be used in the design.

Requirements
Must have
• Space for:
• 2 addresses (a PO Box Address and a consulting suite address) - to be confirmed
• 1 phone number - to be confirmed
Nice to have
• Please choose one of the FCWES logos (I included 3 - colour, black reverse, and greyscale); if you include this in the design, IT SHOULD NOT DOMINATE THE CARD, but be smaller and more discreet.
• I have also attached the FUPelV logo (colour and greyscale); if you choose to include this in the design, IT SHOULD NOT DOMINATE THE CARD, but be smaller and more discreet.
• I would love to be able to update details on the card as time goes on, and thus would like to own the template for the card as well.
• Also I would love discussion with regard to any changes on the card, if I am not completely happy with the design, and would like to discuss things such as ease of printing, finish on the cards (matte, polish) etc.
Should not have
• I don't like the card to look too crowded

```html
<!DOCTYPE html>
<html lang="en">
<head>
<meta charset="utf-8">
<title>Dr Mira Thalen – Business Card</title>
<link rel="stylesheet" href="https://fonts.googleapis.com/css2?family=Montserrat:wght@300;400;600&family=Open+Sans:wght@400&display=swap">
<style>
  :root {
    --band: #000000;
    --paper: #efefef;
    --ink: #1a1a1a;
    --white: #ffffff;
    --bone-light: #9a9a9a;
    --bone-dark: #0d0d0d;
  }
  * { margin: 0; padding: 0; box-sizing: border-box; }
  html, body {
    width: 1200px; height: 692px; overflow: hidden;
    background: var(--paper);
  }
  .card {
    position: relative; width: 1200px; height: 692px;
    background: var(--paper); color: var(--ink);
  }
  .header-band {
    position: absolute; left: 0; top: 0; width: 1200px; height: 364px;
    background: var(--band);
  }
  .name {
    position: absolute; left: 75px; top: 104px;
    font-family: "Montserrat", sans-serif; font-weight: 600;
    font-size: 57px; letter-spacing: 1px; color: var(--white);
    text-transform: uppercase; line-height: 1;
  }
  .role {
    position: absolute; left: 76px; top: 176px;
    font-family: "Montserrat", sans-serif; font-weight: 400;
    font-size: 30px; letter-spacing: 1.5px; color: var(--white);
    text-transform: uppercase; line-height: 1;
  }
  .credentials {
    position: absolute; left: 77px; top: 236px;
    font-family: "Open Sans", sans-serif; font-weight: 400;
    font-size: 19px; color: var(--white); line-height: 1;
  }
  .xray-area {
    position: absolute; left: 712px; top: 14px; width: 410px; height: 350px;
    background: radial-gradient(ellipse at 25% 55%, var(--bone-light) 0%, #3a3a3a 35%, var(--bone-dark) 65%),
                radial-gradient(ellipse at 75% 55%, var(--bone-light) 0%, #3a3a3a 35%, transparent 65%);
    background-blend-mode: lighten;
  }
  .contact {
    position: absolute; display: flex; align-items: center;
    font-family: "Montserrat", sans-serif; font-weight: 300;
    font-size: 25px; letter-spacing: 1px; font-variant: small-caps;
    color: var(--ink);
  }
  .contact .icon { width: 44px; height: 70px; margin-right: 38px; flex: none; }
  .contact--address-1 { left: 76px; top: 418px; }
  .contact--address-2 { left: 76px; top: 558px; }
  .contact--phone { left: 662px; top: 418px; }
  .contact--phone .icon { width: 52px; height: 70px; margin-right: 30px; }
  .fellowship {
    position: absolute; display: flex; align-items: center; gap: 10px;
    font-family: "Montserrat", sans-serif; font-weight: 400;
    font-size: 26px; color: var(--ink);
  }
  .fellowship .mark {
    width: 48px; height: 48px; border: 2px solid var(--ink);
  }
  .fellowship--college { left: 730px; top: 608px; }
  .fellowship--association { left: 1030px; top: 608px; }
</style>
</head>
<body>
<div class="card">
  <div class="header-band"></div>
  <h1 class="name">Dr Mira Thalen</h1>
  <p class="role">Orthopaedic Hand Surgeon</p>
  <p class="credentials">MBBS BSc (Med), MIntPH (Merit), FCWES (Ortho), FUPelV</p>
  <div class="xray-area" role="img" aria-label="X-ray image of two hands, palms down, on black"></div>

  <div class="contact contact--address-1">
    <svg class="icon" viewBox="0 0 44 70" aria-hidden="true"><path d="M22 0C10 0 0 10 0 22c0 16 22 48 22 48s22-32 22-48C44 10 34 0 22 0zm0 31a9 9 0 1 1 0-18 9 9 0 0 1 0 18z" fill="#111"/></svg>
    <span>Address 1 will come here</span>
  </div>
  <div class="contact contact--address-2">
    <svg class="icon" viewBox="0 0 44 70" aria-hidden="true"><path d="M22 0C10 0 0 10 0 22c0 16 22 48 22 48s22-32 22-48C44 10 34 0 22 0zm0 31a9 9 0 1 1 0-18 9 9 0 0 1 0 18z" fill="#111"/></svg>
    <span>Address 2 will come here</span>
  </div>
  <div class="contact contact--phone">
    <svg class="icon" viewBox="0 0 52 52" aria-hidden="true"><path d="M11 2c2-1 4 0 5 2l6 10c1 2 0 4-1 5l-4 3c2 6 8 12 14 14l3-4c1-1 3-2 5-1l10 6c2 1 3 3 2 5l-3 6c-1 2-3 3-6 3C22 50 2 30 2 11c0-3 1-5 3-6z" fill="#111"/></svg>
    <span>Mobile num. will come here</span>
  </div>

  <div class="fellowship fellowship--college"><span class="mark"></span><span>FCWES</span></div>
  <div class="fellowship fellowship--association"><span class="mark"></span><span>FUPelV</span></div>
</div>
</body>
</html>
```